Lumeno-Interior design firm
Hello all,
I will announce the winner in the next few hours...
I appreciate your AMAZING ideas and all the many revisions that each of you submited, they helped us to understand your creative proposals and at the end to select a winner.
THANK YOU!
Lumeno Design
Draft #317 and #318
We are looking at some winning designs already and we will send our efforts towards those. i appreciate your entry very much.
Thanks!
Draft #312
The font on the subject LUMENO Interior design firm needs to be changed. I dont like it. I like the font used on the HOME, PORTFOLIO, etc...main subjects if that helps!
Everything else looks amazing!
hi all,
I had an unexpected business to attend today and I was not able to complete the feedback to all of you. We decided to extend the time to provide the missing feedback...I will provide to all, just give me some time.
I have decided to extend the contest. This was a last minute descision.
I appreciate your entry but is not what I am looking for. I don't want to waste your time as well as I prefer to concentrate on the designs/designers that have invested some time with me already.
Thank you and I appreciate your understanding!
Thanks brightquill! I really appreciate your understanding!
Draft #273
Can you justified all the texts used on each page? That will be great for final review.
Drafts #270 and #272
the text needs to be justified and that will make it!
Draft #269
HOME
There is a small misspell at the bottom left...it reads Lemeno instead of Lumeno.
Ater that revision you are set!
@PH, Thanks for your comments...
Dear Brightquill,
I like your entry but i am sorry to say that there is nothing original about it. I feel respect for everyones work and even when I am not an expert I feel you are copying other entries. I can not give you credit for someone else's ideas and I would appreciate if you come up with the same concept but with something that is your very own creation.
With all my respect...
Draft #251
Looks good just to revise the "yellow" cubes to be softer...and also please use my pictures for each page so I can compare with everyone else.
Thank you so much!
Draft #250
I would prefer to container the ABOUT US description on within the limits of the cubes so if necessary lets remove the "yellow" cubes so we can move up the wording and fit it within...
Use the service wording as reference...it is contained and it does not go below the "cubes"
Draft #249
lets list the services on a horizontal way inside the "cubes" Makes sense? linear way showing the services and the main wording as is.
Draft #248
can we made the windows with tabs LIVING, DINING, BEDROOM ACCENTS and KIDS to be one of the "cubes" from your design?
maybe using the bottom five...?
then when you click on I would like to see a complete picture...hopefully you come up with an idea but if not we can look at it together after revision...
Thanks
Draft #247
My only change is the "yellow" buttons to be more with softer colors...soft grey/white...or any suggestions within my request.
Draft #234
Wording needs to be consistent...I prefer white please revise.
Draft #227
Revisions:
I dont like the phone image under phone, please remove
Please do not underline the website
I prefer just letter on the front:
P: for phone
W: for website
etc...
In your case I would prefer not to use my picture...lets just remove it and after all this it should be done!
Looking good!
Draft #223
I need you to add the wording that I sent for services as well...it is important!
Thanks! Everything else looks perfect!
Hello@PH
I`m just waiting for your Feedback on
#221(Home page), #222(Portfolio Page), #223(Services Page),#224(About Us Page), & #225(Contact Page)
Zora
FOR EVERYONE:
PLEASE submit your complete designs, I wont be extending the project and with the time left I wont be able to give feedback and revisions to detail to everyone.
I really appreciate your hard work on attention to my project.
You ALL are very talented!
Good luck!
Draft #208 you can move forward with the inner pages.
Draft #207
I need the text to be justified please. You can complete your design with all he pages, I like the layout as is.
Look forward to final entries.

```html
<!DOCTYPE html>
<html lang="en">
<head>
<meta charset="utf-8">
<title>Lumeno Design – Services</title>
<link rel="stylesheet" href="https://fonts.googleapis.com/css2?family=Arimo:wght@400;700&display=swap">
<style>
  :root {
    --canvas: #dcdcdc;
    --canvas-light: #ececec;
    --logo-tile: #e4e2dc;
    --logo-ink: #7a6a4f;
    --frame: #ffffff;
    --nav-bg: rgba(58, 40, 26, 0.72);
    --nav-active: rgba(196, 160, 112, 0.85);
    --nav-ink: #ffffff;
    --overlay-bg: rgba(40, 34, 28, 0.72);
    --accent: #d9a55b;
    --body-ink: #f2efe9;
    --footer-ink: #7d7d7d;
    --icon: #9a9a9a;
  }
  * { margin: 0; padding: 0; box-sizing: border-box; }
  html, body { width: 1200px; height: 718px; overflow: hidden; }
  body {
    position: relative;
    font-family: "Arimo", Arial, sans-serif;
    background: var(--canvas);
  }
  .backdrop {
    position: absolute; inset: 0;
    background: radial-gradient(ellipse at 50% 45%, var(--canvas-light) 0%, var(--canvas) 70%, #cfcfcf 100%);
  }
  .brand-tile {
    position: absolute; left: 713px; top: 0; width: 223px; height: 108px;
    background: var(--logo-tile);
    display: flex; align-items: center; justify-content: center; gap: 12px;
  }
  .brand-mark { width: 30px; height: 30px; background: var(--logo-ink); opacity: .55; }
  .brand-name {
    font-size: 30px; font-weight: 400; color: var(--logo-ink); letter-spacing: 2px; line-height: 1;
  }
  .brand-tagline { display: block; font-size: 9px; letter-spacing: .5px; margin-top: 4px; }
  .stage {
    position: absolute; left: 137px; top: 108px; width: 929px; height: 521px;
    border: 6px solid var(--frame);
    box-shadow: 0 2px 8px rgba(0,0,0,.25);
    overflow: hidden;
  }
  .hero-photo {
    position: absolute; inset: 0;
    background: linear-gradient(180deg, #7a5a38 0%, #a07a4d 10%, #5c7a3e 22%, #3f6a2c 45%, #6d8a45 60%, #8a7560 75%, #b0a28e 100%);
  }
  .main-nav {
    position: absolute; left: 630px; top: 0; width: 160px; height: 160px;
    background: var(--nav-bg);
    padding-top: 6px;
  }
  .main-nav a {
    display: block; text-align: right; padding: 0 30px 0 0;
    height: 26px; line-height: 26px;
    color: var(--nav-ink); text-decoration: none; font-size: 12px; font-weight: 700; letter-spacing: .3px;
  }
  .main-nav a.is-active { background: var(--nav-active); }
  .services-panel {
    position: absolute; left: 6px; bottom: 6px; width: 907px; height: 130px;
    background: var(--overlay-bg);
    padding: 12px 20px 0 20px;
    color: var(--body-ink);
  }
  .services-title { font-size: 18px; font-weight: 400; color: var(--accent); margin-bottom: 8px; }
  .service-list {
    list-style: none; display: grid;
    grid-template-columns: 198px 198px 212px 200px;
    row-gap: 6px; font-size: 11px;
  }
  .service-list li::before { content: "■"; color: var(--accent); font-size: 7px; margin-right: 6px; vertical-align: 2px; }
  .services-copy { margin-top: 14px; font-size: 10px; line-height: 15px; text-align: justify; }
  .footer-brand {
    position: absolute; left: 156px; top: 648px;
    display: flex; align-items: center; gap: 8px;
  }
  .footer-brand .brand-mark { width: 20px; height: 20px; background: var(--footer-ink); }
  .footer-brand .brand-name { font-size: 20px; color: var(--footer-ink); letter-spacing: 1px; }
  .footer-nav { position: absolute; right: 140px; top: 652px; display: flex; gap: 18px; }
  .footer-nav a { color: var(--footer-ink); font-size: 11px; text-decoration: none; }
  .social { position: absolute; left: 1016px; top: 676px; display: flex; gap: 8px; }
  .social span { width: 16px; height: 16px; background: var(--icon); display: block; }
</style>
</head>
<body>
  <div class="backdrop" role="img" aria-label="Soft grey backdrop with faint white branch silhouettes"></div>

  <header class="brand-tile">
    <span class="brand-mark"></span>
    <span class="brand-name">LUMENO<span class="brand-tagline">Interior design firm</span></span>
  </header>

  <main class="stage">
    <div class="hero-photo" role="img" aria-label="Photo of a backyard patio under a wooden pergola with a dining table, chairs and lanterns, lawn and fence behind"></div>

    <nav class="main-nav">
      <a href="#">HOME</a>
      <a href="#">PORTFOLIO</a>
      <a href="#">ABOUT US</a>
      <a href="#" class="is-active">SERVICES</a>
      <a href="#">CONTACT US</a>
    </nav>

    <section class="services-panel">
      <h2 class="services-title">Services</h2>
      <ul class="service-list">
        <li>Interior Design</li>
        <li>Architectural Consulting</li>
        <li>Art Selection</li>
        <li>Textiles</li>
        <li>Furniture Import and Export</li>
        <li>Staging</li>
        <li>Accessories</li>
      </ul>
      <p class="services-copy">As an additional service, we offer a turn key design service that integrates all elements of interior and exterior design including space planning, furnishing, lighting and decor. We will take care of purchasing everything from A to Z, hang your art pieces, and purchase your china so when you get to your new home, the beds are made, the candles are lit and everything is in place to live and enjoy!</p>
    </section>
  </main>

  <footer>
    <div class="footer-brand">
      <span class="brand-mark"></span>
      <span class="brand-name">LUMENO</span>
    </div>
    <nav class="footer-nav">
      <a href="#">Home</a>
      <a href="#">Portfolio</a>
      <a href="#">About us</a>
      <a href="#">Services</a>
      <a href="#">Contact us</a>
    </nav>
    <div class="social"><span></span><span></span></div>
  </footer>
</body>
</html>
```